Founder / concept developer needs business card // Consultant needs VCARD

I need a business card for me as a founding consultant in Berlin. I advise entrepreneurs, especially in the design of business ideas, business plans or financing applications. More information about this in the annexes. My USP: I design / structure complex ideas and projects convincingly so that my client is successful. I want to communicate professionalism, effectiveness and clarity. Colors like from the range BLACK-GRAY-GREEN. I am 27 years old, I have studied business for 7 years. Attachments: - Business card design (only idea, do not focus on it) - Website screenshot (only idea, do not focus on it)

Target Market(s)

Target group: Founder (20-50 yrs, m / w, needy, in "break-up phase") and CONTRACTOR / "financier" (30-55 yrs, m / w, often public service "routine-oriented"). The foundations are in quite different industries: digital, craft, tourism, retail, services, etc. Almost all German.

Industry/Entity Type

Consultant

Contact Information for Business Card

Lukas Brenner
M. Sc., International Business Administration
Gründungsberater, Konzeptentwickler
www.falkor-plan.de
kontakt@falkor-plan.de
Tel. 0157 284 3361

Colors

Designer to choose colors to be used in the design.

Requirements
Must have
• Professionalism, persuasiveness, clarity
Nice to have
• memorability
Should not have
• Schnörkelei

```html
<!DOCTYPE html>
<html lang="de">
<head>
<meta charset="utf-8">
<title>Lukas Brenner – Visitenkarte</title>
<link rel="stylesheet" href="https://fonts.googleapis.com/css2?family=Michroma&family=Roboto+Condensed:wght@300;400&display=swap">
<style>
  :root {
    --canvas: #d9d7d3;
    --paper: #ffffff;
    --ink-grey: #6e6e6e;
    --blue-deep: #053a6b;
    --blue-bright: #0a87b3;
    --black-top: #3a3a3a;
    --black-bottom: #050505;
    --white: #ffffff;
    --url-grey: #9a9a9a;
  }
  * { margin: 0; padding: 0; box-sizing: border-box; }
  html, body { width: 1200px; height: 780px; overflow: hidden; }
  body {
    background: var(--canvas);
    font-family: "Roboto Condensed", sans-serif;
    position: relative;
  }
  .card {
    position: absolute;
    top: 225px;
    width: 540px;
    height: 330px;
    overflow: hidden;
    box-shadow: 0 6px 18px rgba(0,0,0,.25);
  }
  /* Front */
  .card--front { left: 40px; background: var(--paper); }
  .contact {
    position: absolute;
    top: 30px;
    right: 350px;
    text-align: right;
    font-style: normal;
    font-weight: 400;
    font-size: 15px;
    line-height: 22px;
    letter-spacing: .5px;
    color: var(--ink-grey);
    text-transform: uppercase;
    white-space: nowrap;
  }
  .name-band {
    position: absolute;
    left: 200px;
    right: 0;
    top: 118px;
    height: 84px;
    background: linear-gradient(100deg, var(--blue-deep) 0%, var(--blue-deep) 35%, var(--blue-bright) 100%);
    display: flex;
    align-items: center;
    padding-left: 26px;
    padding-right: 16px;
  }
  .name {
    font-family: "Michroma", sans-serif;
    font-weight: 400;
    font-size: 21px;
    color: var(--white);
    letter-spacing: .3px;
    white-space: nowrap;
  }
  .credentials {
    position: absolute;
    top: 222px;
    left: 226px;
    font-weight: 300;
    font-size: 16px;
    line-height: 22px;
    color: var(--ink-grey);
    white-space: nowrap;
  }
  /* Back */
  .card--back {
    left: 620px;
    background: radial-gradient(ellipse at 40% 20%, var(--black-top) 0%, #1a1a1a 45%, var(--black-bottom) 100%);
  }
  .brand-block {
    position: absolute;
    left: 0;
    top: 118px;
    width: 200px;
    height: 84px;
    background: linear-gradient(100deg, var(--blue-deep) 0%, #0a5f94 100%);
    display: flex;
    align-items: center;
    justify-content: center;
  }
  .brand-name {
    font-family: "Michroma", sans-serif;
    font-size: 16px;
    color: var(--white);
    letter-spacing: 2px;
  }
  .back-url {
    position: absolute;
    right: 34px;
    bottom: 40px;
    font-weight: 300;
    font-size: 17px;
    letter-spacing: 7px;
    color: var(--url-grey);
    text-transform: uppercase;
    white-space: nowrap;
  }
</style>
</head>
<body>
  <section class="card card--front">
    <address class="contact">
      0157 284 3361<br>
      kontakt@falkor-plan.de<br>
      www.falkor-plan.de
    </address>
    <div class="name-band"><h1 class="name">LUKAS BRENNER</h1></div>
    <p class="credentials">
      M. Sc., International Business Administration<br>
      Gründungsberater, Konzeptentwickler
    </p>
  </section>

  <section class="card card--back">
    <div class="brand-block"><span class="brand-name">FALKOR</span></div>
    <p class="back-url">www.falkor-plan.de</p>
  </section>
</body>
</html>
```